Adventskalender
Zielgruppe
Männer im Alter zwischen 29 u. 49 Jahren, hohe Bildung, höheres Einkommen, sehr modeaffin.
Varos-Segmente: Moderne Performer, Postmateriell und Etablierte.
Aufgabenstellung
Wir wünschen uns die Gestaltung eines Adventskalenders, den wir im Dezember im Rahmen einer Aktion auf unseren Seiten verwenden möchten.
Gestaltet werden sollen zwei Typen von Seiten (siehe Screenshots):
1. Adventskalender
2. Detailseite nach Klick auf ein Türchen mit Gewinn und der Aufgabe für diesen Tag

```html
<!DOCTYPE html>
<html lang="de">
<head>
<meta charset="utf-8">
<title>Online Adventskalender – modehaus-nordhof.de</title>
<link href="https://fonts.googleapis.com/css2?family=Arimo:wght@400;700&family=Libre+Baskerville&display=swap" rel="stylesheet">
<style>
:root{
  --page-bg:#0c2f63;
  --navy:#0f2a56;
  --ink:#123a78;
  --white:#ffffff;
  --accent:#c8d84a;
  --red:#c8102e;
  --door:#eef0f4;
  --line:#c9c9c9;
  --grey:#8a8a8a;
  --hotline:#6a2b86;
}
*{box-sizing:border-box;margin:0;padding:0}
html,body{width:969px;height:1200px;overflow:hidden}
body{background:var(--page-bg);font-family:"Arimo",Arial,sans-serif;position:relative}
.abs{position:absolute}
.header{left:112px;top:0;width:745px;height:45px;background:var(--white)}
.brand{left:10px;top:9px;display:flex;align-items:center;gap:6px;font:700 20px "Arimo",sans-serif;color:var(--navy)}
.brand i{width:16px;height:16px;border-radius:50%;background:var(--navy);display:block}
.badge{left:440px;top:-40px;width:110px;height:80px;border-radius:50%;background:#e4e7ee;font-size:8px;color:var(--ink);text-align:center;padding-top:42px;line-height:10px}
.hotline{right:10px;top:12px;text-align:right;font-size:8.5px;color:var(--hotline);line-height:12px}
.nav{left:112px;top:45px;width:745px;height:17px;background:var(--navy);font-size:9px;color:var(--white)}
.nav span{position:absolute;top:3px;white-space:nowrap}
.nav .sep{border-left:1px solid #5a6f95;padding-left:5px}
.nav .hl{color:var(--accent)}
.sidebar{left:121px;top:69px;list-style:none;font-size:10.5px;line-height:15.6px;color:var(--white)}
.content{left:220px;top:62px;width:637px;height:1012px;background:var(--white)}
.title{left:13px;top:8px;font:28px "Libre Baskerville",serif;color:var(--navy);white-space:nowrap}
.intro{left:13px;top:50px;width:420px;font-size:9.5px;font-weight:700;color:var(--ink);line-height:11.5px}
.social{right:12px;top:10px;display:flex;gap:10px;align-items:center;font-size:9px;color:var(--grey)}
.like{border:1px solid #aab;padding:2px 5px;background:#f3f4f7;color:#333;display:flex;gap:4px;align-items:center}
.like b{width:8px;height:8px;background:#8aa;display:block}
.calendar{left:11px;top:110px;width:615px;height:371px;background:radial-gradient(ellipse at 50% 60%,#4e7ec0,#1d4a8a 55%,#123a72);border:1px solid #c7b860}
.door{position:absolute;width:71px;height:71px;background:var(--door);border:1px solid #c7b860;display:flex;align-items:center;justify-content:center;font:31px "Libre Baskerville",serif;color:var(--red)}
.door.opened{background:#a9b8cc;opacity:.75;border-color:#9fb0c6}
.door.today{background:var(--red);color:var(--white)}
.gift{left:-11px;top:427px;width:50px;height:62px;background:#c0141c}
.bow{left:540px;top:463px;width:84px;height:70px;background:radial-gradient(#f4f4f4,#b9b9b9);border-radius:40%}
.prize{left:11px;top:489px;width:615px;height:64px;background:linear-gradient(#2f5d9b,#123a72);color:var(--white);font:19px "Libre Baskerville",serif;line-height:25px;padding:7px 10px}
.slot{position:absolute;width:302px;height:213px;border:1px solid var(--line)}
.slot svg{position:absolute;inset:0;width:100%;height:100%}
.slot span{position:absolute;left:0;right:0;top:50%;transform:translateY(-50%);text-align:center;font-size:8.5px;color:var(--grey);background:var(--white);line-height:11px;padding:2px 0}
.footer{left:220px;top:1078px;width:637px;height:70px;background:var(--white);border-top:1px solid #ddd}
.foot-brand{left:11px;top:16px;font:700 12px "Arimo",sans-serif;color:var(--navy);white-space:nowrap}
.foot-brand small{display:block;font-size:6.5px;font-weight:400;color:#333;line-height:9px}
.usp{left:156px;top:9px;font-size:8.5px;color:var(--grey);line-height:14px}
.usp b{color:var(--navy)}
.legal{left:224px;top:1156px;width:630px;font-size:8.5px;color:var(--white);line-height:13px}
.legal b{margin-right:10px}
.copy{right:0;top:0}
</style>
</head>
<body>
<header class="header abs">
  <div class="brand abs"><i></i>modehaus-nordhof.de</div>
  <div class="badge abs">· keine Versandkosten<br>· 180 aktuelle<br>Top-Marken</div>
  <div class="hotline abs">GEBÜHRENFREIE HERRENMODEBERATUNG<br>Tel: 0800 / 123 45 67 | Mo-Fr: 08:00 - 18:00</div>
</header>
<nav class="nav abs">
  <span class="hl" style="left:9px">GESAMTAUSWAHL</span>
  <span class="sep" style="left:112px">HOME</span>
  <span class="sep" style="left:151px">NEU</span>
  <span class="sep" style="left:182px">SALE</span>
  <span class="sep" style="left:219px">KONTAKT</span>
  <span class="sep" style="left:276px">BLOG</span>
  <span class="sep" style="left:313px">HERRENMODE - HANDBUCH</span>
  <span class="sep" style="left:543px">MERKZETTEL</span>
  <span class="sep" style="left:613px">IHR KONTO</span>
  <span class="sep hl" style="left:677px">Einkaufskorb</span>
</nav>
<ul class="sidebar abs">
  <li>Accessoires</li><li>Anzüge / Sakkos</li><li>Gürtel</li><li>Hemden</li><li>Hosen</li><li>Jacken / Mäntel</li><li>Jeans</li><li>Krawatten</li><li>Nachtwäsche / Bad</li><li>Polos</li><li>Pullover</li><li>Schuhe</li><li>Socken</li><li>Sportswear / Sport</li><li>T-Shirts</li><li>Unterwäsche</li>
</ul>
<main class="content abs">
  <h1 class="title abs">Online Adventskalender</h1>
  <div class="social abs"><span>Zwitscher</span><span class="like"><b></b>Gefällt mir</span></div>
  <p class="intro abs">In unserem Online Adventskalender warten jeden Tag eine neue Weihnachts-<br>Überraschung auf Sie - unter anderem Beispiel 1, Beispiel 2 oder Beispiel 3.<br>Zudem eine Verlosung von Preisen unter allen Teilnehmern!<br><br>Also mitraten und gewinnen!</p>
  <section class="calendar abs" role="img" aria-label="Adventskalender mit 24 Türchen vor blauem Hintergrund mit Weihnachtsbaum aus Sternen">
    <div class="door opened" style="left:29px;top:11px">1</div>
    <div class="door today" style="left:126px;top:11px">2</div>
    <div class="door" style="left:223px;top:11px">3</div>
    <div class="door" style="left:320px;top:11px">4</div>
    <div class="door" style="left:417px;top:11px">5</div>
    <div class="door" style="left:514px;top:11px">6</div>
    <div class="door" style="left:29px;top:103px">7</div>
    <div class="door" style="left:126px;top:103px">8</div>
    <div class="door" style="left:223px;top:103px">9</div>
    <div class="door" style="left:320px;top:103px">10</div>
    <div class="door" style="left:417px;top:103px">11</div>
    <div class="door" style="left:514px;top:103px">12</div>
    <div class="door" style="left:29px;top:196px">13</div>
    <div class="door" style="left:126px;top:196px">14</div>
    <div class="door" style="left:223px;top:196px">15</div>
    <div class="door" style="left:320px;top:196px">16</div>
    <div class="door" style="left:417px;top:196px">17</div>
    <div class="door" style="left:514px;top:196px">18</div>
    <div class="door" style="left:29px;top:287px">19</div>
    <div class="door" style="left:126px;top:287px">20</div>
    <div class="door" style="left:223px;top:287px">21</div>
    <div class="door" style="left:320px;top:287px">22</div>
    <div class="door" style="left:417px;top:287px">23</div>
    <div class="door" style="left:514px;top:287px">24</div>
  </section>
  <div class="gift abs" role="img" aria-label="Rotes Geschenkpaket"></div>
  <div class="prize abs">Und unter allen Teilnehmern verlosen wir:<br>Gutscheine im Wert von jeweils 100 Euro</div>
  <div class="bow abs" role="img" aria-label="Silberne Geschenkschleife"></div>
  <div class="slot" style="left:13px;top:563px"><svg viewBox="0 0 100 100" preserveAspectRatio="none"><path d="M0 0L100 100M100 0L0 100" stroke="#c9c9c9" stroke-width=".5" vector-effect="non-scaling-stroke"/></svg><span>KURZNACHRICHTEN-STREAM</span></div>
  <div class="slot" style="left:324px;top:563px"><svg viewBox="0 0 100 100" preserveAspectRatio="none"><path d="M0 0L100 100M100 0L0 100" stroke="#c9c9c9" stroke-width=".5" vector-effect="non-scaling-stroke"/></svg><span>FREUNDESBUCH LIKE-BOX</span></div>
  <div class="slot" style="left:13px;top:784px"><svg viewBox="0 0 100 100" preserveAspectRatio="none"><path d="M0 0L100 100M100 0L0 100" stroke="#c9c9c9" stroke-width=".5" vector-effect="non-scaling-stroke"/></svg><span>FORMULAR ZUR WEITEREMPFEHLUNG<br>PER E-MAIL</span></div>
  <div class="slot" style="left:324px;top:784px"><svg viewBox="0 0 100 100" preserveAspectRatio="none"><path d="M0 0L100 100M100 0L0 100" stroke="#c9c9c9" stroke-width=".5" vector-effect="non-scaling-stroke"/></svg><span>TEXT RECHTLICHES / DISCLAIMER</span></div>
</main>
<footer class="footer abs">
  <div class="foot-brand abs">modehaus-nordhof.de<small>Das Original. Seit 1997.</small></div>
  <div class="usp abs"><b>Herrenmode im Online Shop für Herren</b><br>· Kostenloser Versand<br>· 30 Tage Rückgaberecht<br>· Günstig kaufen</div>
</footer>
<div class="legal abs">
  <b>UNSERE AGB</b><b>DATENSCHUTZBESTIMMUNG</b><b>IMPRESSUM</b><br>
  HERRENMODE · ALLE MARKEN · ALLE KATEGORIEN · AKTUELLE MÄNNERMODE
  <span class="copy abs">© seit 1997 Lindqvist AG</span>
</div>
</body>
</html>
```